Luxury travel advisor business card

I am looking for business cards to highlight my job as a luxury travel advisor. I don't book flights, I create experiences, so nothing that involves imagery of a plane. Nothing too bright that resembles cheap travel magazines with palm trees and beaches. I was thinking darker colours like dark green or even black but I am definitely open to suggestions as long as they fit in the luxury travel brand. I would like some imagery but happy to try designs without.
Target Market(s)
luxury travel market, upscale clients
Industry/Entity Type
travel
Contact Information for Business Card
Dara Kellsworth email:dara.kellsworth@vantrelo.example and the words Vantrelo Travel Advisor phone number: +44 (0) 77184026351
Requirements
Must have
- Bleed Area: 88mm x 59mm Make sure that your background extends to fill the bleed. Trim: 84mm x 55mm Safe Area: 80mm x 51mm
Should not have
- cheap imagery

```html
<!DOCTYPE html>
<html lang="en">
<head>
<meta charset="utf-8">
<title>Dara Kellsworth – Business Card</title>
<link rel="stylesheet" href="https://fonts.googleapis.com/css2?family=Marcellus&display=swap">
<style>
  :root {
    --page-bg: #e9e8e4;
    --card-bg: #06130a;
    --card-bg-edge: #0a1a0f;
    --gold-dark: #8a6410;
    --gold-mid: #c99a22;
    --gold-light: #f2d868;
    --gold-solid: #d4a935;
    --glyph: #07140b;
  }
  * { margin: 0; padding: 0; box-sizing: border-box; }
  html, body {
    width: 1200px;
    height: 978px;
    overflow: hidden;
    background: var(--page-bg);
  }
  .card {
    position: absolute;
    left: 60px;
    top: 127px;
    width: 1080px;
    height: 724px;
    border-radius: 6px;
    overflow: hidden;
    box-shadow: 0 10px 30px rgba(0,0,0,0.18);
  }
  .card-texture {
    position: absolute;
    inset: 0;
    background: radial-gradient(ellipse at 50% 45%, var(--card-bg-edge) 0%, var(--card-bg) 75%);
  }
  .card-header {
    position: absolute;
    left: 110px;
    top: 80px;
    font-family: "Marcellus", serif;
    color: var(--gold-solid);
  }
  .advisor-name {
    font-size: 56px;
    font-weight: 400;
    line-height: 1.1;
    letter-spacing: 1px;
  }
  .advisor-role {
    margin-top: 10px;
    font-size: 24px;
    font-weight: 400;
    letter-spacing: 5px;
    text-transform: uppercase;
  }
  .header-rule {
    margin-top: 24px;
    width: 120px;
    height: 2px;
    background: var(--gold-solid);
  }
  .contact-list {
    position: absolute;
    left: 110px;
    top: 330px;
    list-style: none;
  }
  .contact-item {
    display: flex;
    align-items: center;
    height: 120px;
    margin-bottom: 40px;
  }
  .contact-icon {
    width: 120px;
    height: 120px;
    flex: none;
  }
  .contact-text {
    margin-left: 50px;
    font-family: "Marcellus", serif;
    background: linear-gradient(180deg, var(--gold-light) 0%, var(--gold-mid) 50%, var(--gold-dark) 100%);
    -webkit-background-clip: text;
    background-clip: text;
    color: transparent;
    white-space: nowrap;
    line-height: 1.3;
  }
  .contact-text.phone { font-size: 52px; letter-spacing: 1px; }
  .contact-text.email { font-size: 42px; }
</style>
</head>
<body>
  <svg width="0" height="0" style="position:absolute">
    <defs>
      <linearGradient id="gold" x1="0" y1="0" x2="1" y2="1">
        <stop offset="0" stop-color="#8a6410"/>
        <stop offset="0.5" stop-color="#f2d868"/>
        <stop offset="1" stop-color="#9a7414"/>
      </linearGradient>
    </defs>
  </svg>

  <section class="card" aria-label="Business card, contact details">
    <div class="card-texture" role="img" aria-label="Faint diamond lattice pattern on deep green-black"></div>

    <header class="card-header">
      <h1 class="advisor-name">Dara Kellsworth</h1>
      <p class="advisor-role">Vantrelo Travel Advisor</p>
      <div class="header-rule"></div>
    </header>

    <ul class="contact-list">
      <li class="contact-item">
        <svg class="contact-icon" viewBox="0 0 100 100" aria-hidden="true">
          <circle cx="50" cy="50" r="48" fill="url(#gold)"/>
          <path fill="var(--glyph)" d="M30 22c3-2 6-2 8 1l6 9c1.5 2.5 1 5-1 7l-3 3c2 6 8 13 14 16l3-3c2-2 4.5-2.5 7-1l9 6c3 2 3 5 1 8l-3 4c-3 4-9 5-15 2-14-7-25-19-31-33-2-6-1-12 3-15z"/>
        </svg>
        <span class="contact-text phone">+44 (0) 77184026351</span>
      </li>
      <li class="contact-item">
        <svg class="contact-icon" viewBox="0 0 100 100" aria-hidden="true">
          <circle cx="50" cy="50" r="48" fill="url(#gold)"/>
          <rect x="20" y="30" width="60" height="40" rx="2" fill="var(--glyph)"/>
          <path d="M23 33l27 21 27-21" fill="none" stroke="url(#gold)" stroke-width="3"/>
          <path d="M23 67l20-17M77 67l-20-17" fill="none" stroke="url(#gold)" stroke-width="3"/>
        </svg>
        <span class="contact-text email">dara.kellsworth@vantrelo.example</span>
      </li>
    </ul>
  </section>
</body>
</html>
```